Lip Balm tube design

create label/ product print design for Lip balm tubes
Size of tube
76 mm high
24 mm wide

2.75 x 2" h- this is for the main part of tube, not top cap

Current design has been attached for reference. Would like to stick to something similar but need it to "pop" more and be more readable to user
Designs
Vanilla Mint
Citrus Spice
Coconut Lime
Marshmallow Creme
Satsuma Sugar

Designs must include product information (ingredients) as detailed on examples.
Color palette is color but soft, matte tones

```html
<!DOCTYPE html>
<html lang="en">
<head>
<meta charset="utf-8">
<title>Terra Bloom Natural Lip Balm – Tube Labels</title>
<link href="https://fonts.googleapis.com/css2?family=Cormorant+Garamond:wght@400;500&family=Libre+Caslon+Text&display=swap" rel="stylesheet">
<style>
  :root {
    --stage: #222833;
    --cream-bg: #f6f0e7;  --cream-ink: #6e6157;
    --grey-bg: #e3e4e8;   --grey-ink: #545468;
    --green-bg: #d7e7c5;  --green-ink: #606b4c;
    --orange-bg: #d7744f; --orange-ink: #ffffff;
    --peach-bg: #f8dcb6;  --peach-ink: #7b6553;
    --title-font: "Cormorant Garamond", serif;
    --text-font: "Libre Caslon Text", serif;
  }
  * { margin: 0; padding: 0; box-sizing: border-box; }
  html, body { width: 1200px; height: 600px; overflow: hidden; }
  body { background: var(--stage); position: relative; }

  .label {
    position: absolute; width: 244px; height: 178px; overflow: hidden;
    background: var(--bg); color: var(--ink);
  }
  .label--marshmallow { --bg: var(--cream-bg); --ink: var(--cream-ink); --badge-bg: var(--cream-ink); --badge-ink: #fff; left: 348px; top: 18px; }
  .label--vanilla     { --bg: var(--grey-bg);  --ink: var(--grey-ink);  --badge-bg: var(--grey-ink);  --badge-ink: #fff; left: 607px; top: 18px; }
  .label--coconut     { --bg: var(--green-bg); --ink: var(--green-ink); --badge-bg: var(--green-ink); --badge-ink: #fff; left: 348px; top: 211px; }
  .label--citrus      { --bg: var(--orange-bg);--ink: var(--orange-ink);--badge-bg: #ffffff;          --badge-ink: var(--orange-bg); left: 607px; top: 211px; }
  .label--satsuma     { --bg: var(--peach-bg); --ink: var(--peach-ink); --badge-bg: var(--peach-ink); --badge-ink: #fff; left: 462px; top: 404px; }

  .label-pattern {
    position: absolute; inset: 0;
    background: radial-gradient(circle at 30% 40%, rgba(255,255,255,0.18), rgba(255,255,255,0) 70%);
  }

  .info-col {
    position: absolute; left: 14px; top: 12px; width: 80px; height: 160px;
    text-align: center; font-family: var(--text-font);
  }
  .brand {
    font-family: var(--text-font); font-size: 9px; line-height: 1;
    padding-bottom: 2px; border-bottom: 0.6px solid var(--ink); display: inline-block;
  }
  .product-type {
    font-family: var(--title-font); font-weight: 400; font-size: 12px;
    line-height: 0.92; margin-top: 4px; letter-spacing: 0.02em;
  }
  .badges { list-style: none; margin-top: 14px; }
  .badge {
    width: 18px; height: 18px; border-radius: 50%; margin: 0 auto 4.5px;
    background: var(--badge-bg); color: var(--badge-ink);
    font-size: 4.2px; line-height: 1.05; display: flex; align-items: center; justify-content: center;
  }
  .origin { position: absolute; left: 0; right: 0; top: 136px; font-size: 4.6px; line-height: 1.25; letter-spacing: 0.04em; }
  .net-weight { position: absolute; left: 0; right: 0; top: 150px; font-size: 4.2px; letter-spacing: 0.04em; }

  .flavour {
    position: absolute; left: 104px; top: 14px; height: 152px;
    writing-mode: vertical-rl; transform: rotate(180deg);
    font-family: var(--title-font); white-space: nowrap;
  }
  .flavour-name { display: block; font-weight: 400; font-size: 30px; line-height: 0.86; letter-spacing: 0; }
  .label--vanilla .flavour-name { font-size: 33px; }
  .label--citrus .flavour-name { font-size: 39px; }
  .label--satsuma .flavour-name { font-size: 31px; }
  .label--marshmallow .flavour-name { font-size: 30px; line-height: 0.9; }
  .flavour-note { display: block; font-family: var(--text-font); font-size: 7px; letter-spacing: 0.42em; margin-left: 3px; }

  .ingredients {
    position: absolute; left: 192px; top: 12px; width: 34px; height: 150px;
    writing-mode: vertical-rl; transform: rotate(180deg);
    font-family: var(--text-font); font-size: 4.2px; line-height: 1.3; text-align: center;
  }
  .side-notes {
    position: absolute; left: 232px; top: 12px; width: 6px; height: 156px;
    writing-mode: vertical-rl; transform: rotate(180deg);
    display: flex; justify-content: space-between;
    font-family: var(--text-font); font-size: 3.2px; letter-spacing: 0.04em;
  }
</style>
</head>
<body>

<article class="label label--marshmallow">
  <div class="label-pattern" role="img" aria-label="Faint leaf-scroll pattern in cream tones"></div>
  <div class="info-col">
    <p class="brand">Terra Bloom</p>
    <h2 class="product-type">NATURAL<br>LIP BALM</h2>
    <ul class="badges"><li class="badge">Plant<br>Based</li><li class="badge">Vegan</li><li class="badge">Cruelty<br>Free</li></ul>
    <p class="origin">MADE IN CANADA<br>100% NATURAL</p>
    <p class="net-weight">NET WT. 3 OZ/ 8.5 G</p>
  </div>
  <h1 class="flavour"><span class="flavour-name">MARS<br>MALLOW</span><span class="flavour-note">CREME</span></h1>
  <p class="ingredients">Organic Olive Fruit Oil (Olea Europaea), Organic Coconut Oil (Cocos Nucifera), Organic Shea Butter (Butyrospermum Parkii), Organic Jojoba Seed Oil (Simmondsia Chinensis), Rosehip Seed Oil (Rosa Canina), Vitamin E (Tocopherol), Sunflower Seed Oil (Helianthus Annuus), Vanilla Aroma, Dipteryx Odorata (Tonka Bean) Oil.</p>
  <div class="side-notes"><span>WWW.TERRABLOOM.CA</span><span>MADE BY TERRA BLOOM, RIVERTON, AB T0A 1B2</span></div>
</article>

<article class="label label--vanilla">
  <div class="label-pattern" role="img" aria-label="Faint leaf-scroll pattern in soft grey tones"></div>
  <div class="info-col">
    <p class="brand">Terra Bloom</p>
    <h2 class="product-type">NATURAL<br>LIP BALM</h2>
    <ul class="badges"><li class="badge">Plant<br>Based</li><li class="badge">Vegan</li><li class="badge">Cruelty<br>Free</li></ul>
    <p class="origin">MADE IN CANADA<br>100% NATURAL</p>
    <p class="net-weight">NET WT. 3 OZ/ 8.5 G</p>
  </div>
  <h1 class="flavour"><span class="flavour-name">VANILLA</span><span class="flavour-note">MINT</span></h1>
  <p class="ingredients">Organic Olive Fruit Oil (Olea Europaea), Organic Coconut Oil (Cocos Nucifera), Organic Shea Butter (Butyrospermum Parkii), Organic Jojoba Seed Oil (Simmondsia Chinensis), Rosehip Seed Oil (Rosa Canina), Vitamin E (Tocopherol), Sunflower Seed Oil (Helianthus Annuus), Vanilla Aroma, Mentha Piperita (Peppermint) Leaf Oil, Dipteryx Odorata (Tonka Bean) Oil.</p>
  <div class="side-notes"><span>WWW.TERRABLOOM.CA</span><span>MADE BY TERRA BLOOM, RIVERTON, AB T0A 1B2</span></div>
</article>

<article class="label label--coconut">
  <div class="label-pattern" role="img" aria-label="Faint leaf-scroll pattern in pale green tones"></div>
  <div class="info-col">
    <p class="brand">Terra Bloom</p>
    <h2 class="product-type">NATURAL<br>LIP BALM</h2>
    <ul class="badges"><li class="badge">Plant<br>Based</li><li class="badge">Vegan</li><li class="badge">Cruelty<br>Free</li></ul>
    <p class="origin">MADE IN CANADA<br>100% NATURAL</p>
    <p class="net-weight">NET WT. 3 OZ/ 8.5 G</p>
  </div>
  <h1 class="flavour"><span class="flavour-name">COCONUT</span><span class="flavour-note">LIME</span></h1>
  <p class="ingredients">Organic Olive Fruit Oil (Olea Europaea), Organic Coconut Oil (Cocos Nucifera), Organic Shea Butter (Butyrospermum Parkii), Organic Jojoba Seed Oil (Simmondsia Chinensis), Rosehip Seed Oil (Rosa Canina), Vitamin E (Tocopherol), Sunflower Seed Oil (Helianthus Annuus), Vanilla Aroma, Lime (Citrus Hystrix), Lemongrass (Cymbopogon Citratus) Oil.</p>
  <div class="side-notes"><span>WWW.TERRABLOOM.CA</span><span>MADE BY TERRA BLOOM, RIVERTON, AB T0A 1B2</span></div>
</article>

<article class="label label--citrus">
  <div class="label-pattern" role="img" aria-label="Faint leaf-scroll pattern in terracotta tones"></div>
  <div class="info-col">
    <p class="brand">Terra Bloom</p>
    <h2 class="product-type">NATURAL<br>LIP BALM</h2>
    <ul class="badges"><li class="badge">Plant<br>Based</li><li class="badge">Vegan</li><li class="badge">Cruelty<br>Free</li></ul>
    <p class="origin">MADE IN CANADA<br>100% NATURAL</p>
    <p class="net-weight">NET WT. 3 OZ/ 8.5 G</p>
  </div>
  <h1 class="flavour"><span class="flavour-name">CITRUS</span><span class="flavour-note">SPICE</span></h1>
  <p class="ingredients">Organic Olive Fruit Oil (Olea Europaea), Organic Coconut Oil (Cocos Nucifera), Organic Shea Butter (Butyrospermum Parkii), Organic Jojoba Seed Oil (Simmondsia Chinensis), Rosehip Seed Oil (Rosa Canina), Vitamin E (Tocopherol), Sunflower Seed Oil (Helianthus Annuus), Vanilla Aroma, Mentha Piperita (Peppermint) Leaf Oil, Dipteryx Odorata (Tonka Bean) Oil.</p>
  <div class="side-notes"><span>WWW.TERRABLOOM.CA</span><span>MADE BY TERRA BLOOM, RIVERTON, AB T0A 1B2</span></div>
</article>

<article class="label label--satsuma">
  <div class="label-pattern" role="img" aria-label="Faint leaf-scroll pattern in soft peach tones"></div>
  <div class="info-col">
    <p class="brand">Terra Bloom</p>
    <h2 class="product-type">NATURAL<br>LIP BALM</h2>
    <ul class="badges"><li class="badge">Plant<br>Based</li><li class="badge">Vegan</li><li class="badge">Cruelty<br>Free</li></ul>
    <p class="origin">MADE IN CANADA<br>100% NATURAL</p>
    <p class="net-weight">NET WT. 3 OZ/ 8.5 G</p>
  </div>
  <h1 class="flavour"><span class="flavour-name">SATSUMA</span><span class="flavour-note">SUGAR</span></h1>
  <p class="ingredients">Organic Olive Fruit Oil (Olea Europaea), Organic Coconut Oil (Cocos Nucifera), Organic Shea Butter (Butyrospermum Parkii), Organic Jojoba Seed Oil (Simmondsia Chinensis), Rosehip Seed Oil (Rosa Canina), Vitamin E (Tocopherol), Sunflower Seed Oil (Helianthus Annuus), Vanilla Aroma, Citrus Junos (Yuzu) Leaf Oil, Citrus Paradisi (Grapefruit) Oil.</p>
  <div class="side-notes"><span>WWW.TERRABLOOM.CA</span><span>MADE BY TERRA BLOOM, RIVERTON, AB T0A 1B2</span></div>
</article>

</body>
</html>
```